Stationery Design for Pfotenhaus

We already have a logo a Logo for our outstanding veterinary hospital. Now we are looking for our future letterhead, business cards and envelopes. We would like to see a design using the color from our logo. Additional color should be limited to grey or a rusty brown. The font should be easy and clearly readable and must be easily available on all computers (to install it in our Management software). The finial design should communicate competence in veterinary medicine, and empathy.

To meet the European regulation (DIN5008) there are a couple mandatory legal informations one the letterhead. We also enclosed a template of exact measurement, which need to be respected according to DIN5008.

Mandatory legal information are (best placed in the footer):
"Pfotenhaus GmbH & Co KG, Brunnfeldgasse 417C, 1140 Wien,
Handelsgericht Wien, FN 294617k, GF: Dr. Lorenz Haidinger
ATU 3918462"
Additional informations needed:
"Tel: +43 1 5849162, Fax: +43 1 5849163, info@pfotenhaus-demo.at, www. pfotenhaus-demo.at"
bank account informations should be included as well. These are:
"Sparkasse Hollental Nord, IBAN: AT 58 1111 2222 3333 4444, BIC: HLNTAT2H517"

The Logo should be in the upper right corner. Below that we need a space for informations regarding the responsible veterinarians. There will be 3-5 Names, each of it consisting of 2 lines (see example below). The Names should be highlighted (larger font) compared to the qualifications in the second line.
Tierärztliche Leitung:
Dr. Lorenz Haidinger
Diplomate ECVS
Updates

The contest was startet on the 2nd of may and the deadline was a day later? Why was that so fast? Did I do something wrong? BR

Target Market(s)

dog and cat owner in Austria as welle as referring veterinarians in Austria

Industry/Entity Type

Veterinary

Contact Information for Business Card

One side: Logo
other side:
Dr. Lorenz Haidinger
Diplomate ECVS
EBVS Specialist of Small Animal Surgery

Pfotenhaus GmbH&Co KG
Brunnfeldgasse 417C
1140 Wien

Tel: +43 1 5849160 DW 102
Fax: +43 1 5849160 DW 999
email: lorenz.haidinger@pfotenhaus-demo.at

Font styles to use
Serif
Sans Serif

Requirements
Must have
• The logo should be given in the upper right. Most of the legal informations should be given in the footer. The upper left Area should be clear, since the recipient address will be placed there.
Colors should be limited to golden, blue and greyscale (two different gereysacales at most).

```html
<!DOCTYPE html>
<html lang="de">
<head>
<meta charset="utf-8">
<title>Pfotenhaus – Briefpapier</title>
<link rel="stylesheet" href="https://fonts.googleapis.com/css2?family=Poppins:wght@400;500;600&family=Questrial&display=swap">
<style>
  :root {
    --navy: #172a55;
    --gold: #e0a82a;
    --ink: #222222;
    --grey: #555555;
    --paper-light: #f3f3f3;
    --paper-dark: #e3e3e3;
  }
  * { margin: 0; padding: 0; box-sizing: border-box; }
  html, body { width: 960px; height: 1200px; overflow: hidden; }
  body {
    position: relative;
    background: linear-gradient(100deg, var(--paper-light), var(--paper-dark));
    font-family: "Questrial", "Century Gothic", sans-serif;
    color: var(--ink);
  }
  .header-band {
    position: absolute; left: 0; top: 56px; width: 960px; height: 78px;
    background: var(--navy);
  }
  .brand-mark {
    position: absolute; left: 748px; top: 49px; width: 92px; height: 92px;
    border-radius: 50%; background: var(--navy);
    border: 4px solid var(--gold); box-shadow: 0 0 0 4px #ffffff;
  }
  .brand-name {
    position: absolute; right: 85px; top: 146px;
    font-family: "Poppins", sans-serif; font-weight: 600; font-size: 27px;
    color: var(--navy); letter-spacing: -0.5px; line-height: 1;
  }
  .brand-tagline {
    position: absolute; right: 85px; top: 174px;
    font-family: "Poppins", sans-serif; font-weight: 500; font-size: 12px;
    color: var(--gold); line-height: 1;
  }
  .vet-board {
    position: absolute; right: 91px; top: 192px; text-align: right;
    font-family: "Poppins", sans-serif;
  }
  .vet-board__title { font-size: 14px; font-weight: 500; color: var(--navy); line-height: 1; margin-bottom: 5px; }
  .vet { margin-bottom: 6px; }
  .vet__name { font-size: 13.5px; color: var(--gold); line-height: 16px; }
  .vet__title { font-size: 10px; color: var(--grey); line-height: 11px; }
  .sender-note {
    position: absolute; left: 135px; top: 243px;
    font-size: 13.5px; line-height: 16px; color: var(--ink);
  }
  .sender-ref { position: absolute; left: 135px; top: 300px; font-size: 13.5px; }
  .salutation {
    position: absolute; left: 153px; top: 438px; font-size: 21px;
  }
  .letter-body {
    position: absolute; left: 153px; top: 500px; width: 665px;
    font-size: 12.6px; line-height: 18.3px; text-align: justify; color: var(--ink);
  }
  .letter-body p { margin-bottom: 18.3px; }
  .closing { position: absolute; left: 153px; top: 938px; font-size: 12.6px; }
  .signature {
    position: absolute; left: 176px; top: 962px; width: 128px; height: 66px;
    background: linear-gradient(90deg, rgba(0,0,0,0.06), rgba(0,0,0,0.02));
  }
  .legal-footer {
    position: absolute; left: 0; top: 1100px; width: 960px; text-align: center;
    font-family: "Poppins", sans-serif; font-size: 10.5px; line-height: 17px; color: var(--grey);
  }
  .legal-footer .company { color: var(--navy); }
  .legal-footer svg { width: 10px; height: 10px; vertical-align: -1px; fill: var(--navy); }
</style>
</head>
<body>
  <div class="header-band"></div>
  <div class="brand-mark"></div>
  <div class="brand-name">Pfotenhaus</div>
  <div class="brand-tagline">Fachklinik für Kleintiere</div>

  <div class="vet-board">
    <div class="vet-board__title">Tierärztliche Leitung</div>
    <div class="vet"><div class="vet__name">Dr. Lorenz Haidinger</div><div class="vet__title">Diplomate ECVS</div></div>
    <div class="vet"><div class="vet__name">Dr. Jonas Schmied</div><div class="vet__title">Diplomate ECVS</div></div>
    <div class="vet"><div class="vet__name">Dr. Mirela</div><div class="vet__title">Diplomate ECVS</div></div>
  </div>

  <div class="sender-note">Vivamus faucibus, ipsum nec<br>aliquet viverra, leo mauris condime</div>
  <div class="sender-ref">faucibuspsum</div>

  <div class="salutation">Dear Mr. Berger,</div>

  <div class="letter-body">
    <p>Lorem ipsum dolor sit amet, consectetur adipiscing elit. Donec orci purus, luctus vitae dignissim eu, iaculis sed purus. Vivamus faucibus, ipsum nec aliquet viverra, leo mauris condimentum ligula, sit amet sagittis enim ligula quis arcu. Nam egestas tortor id nisi porttitor mattis. In tortor ante, ultricies in suscipit a, tempus non massa. Vivamus et auctor mi. Fusce vel massa nulla. Phasellus nec eros mauris, et scelerisque orci.</p>
    <p>Donec malesuada orci vitae nulla accumsan porta a id massa. Quisque accumsan iaculis magna sit amet fringilla. Maecenas consequat, magna eget tincidunt semper, odio nibh rutrum mi, id feugiat ante nisi eu risus. Vestibulum nunc orci, rhoncus a placerat in, ultricies in mi. Cras mattis varius eros, vel fringilla nisi suscipit eget. Quisque scelerisque sagittis nulla at porttitor.</p>
    <p>Sed id augue vitae urna euismod commodo aliquet a quam. Pellentesque arcu velit, cursus et malesuada ut, consequat et diam. Nullam erat sem, rhoncus id ullamcorper vitae, rhoncus et arcu. In ultricies ultricies nulla, ut rutrum nisi iaculis at. Donec eu magna a metus ornare faucibus. Fusce aliquet faucibus ultricies. Morbi semper, est id tincidunt gravida, sem arcu adipiscing lacus, ac bibendum nulla leo eu purus. Quisque nec diam sed risus consectetur a ccumsan quis quis nibh. Vestibulum id purus lorem.</p>
    <p>It is a long established fact that a reader will be distracted by the readable content of a page when looking at its layout. The point of using Lorem Ipsum is that it has a more-or-less normal distribution of letters, as opposed to using 'Content here, content here', making it look like readable English. Many desktop publishing packages</p>
  </div>

  <div class="closing">Sincerely,</div>
  <div class="signature" role="img" aria-label="Handwritten signature of the sender"></div>

  <footer class="legal-footer">
    <div><span class="company">Pfotenhaus GmbH &amp; Co KG</span>, Brunnfeldgasse 417C, 1140 Wien, Handelsgericht Wien, FN 294617k</div>
    <div>
      <svg viewBox="0 0 10 10" aria-hidden="true"><path d="M2 0.5 L3.8 2.6 L2.8 3.8 Q3.8 6 6.2 7.2 L7.4 6.2 L9.5 8 L8.3 9.5 Q4.5 9.3 2 6.6 Q0.3 4.5 0.5 1.7 Z"/></svg> +43 1 5849162
      <svg viewBox="0 0 10 10" aria-hidden="true"><rect x="2.5" y="0.5" width="5" height="3"/><rect x="0.5" y="3.5" width="9" height="4" rx="1"/><rect x="2.5" y="7" width="5" height="2.5"/></svg> +43 1 5849163
      <svg viewBox="0 0 10 10" aria-hidden="true"><rect x="0.5" y="2" width="9" height="6.5"/><path d="M0.5 2 L5 5.8 L9.5 2" stroke="#f0f0f0" stroke-width="0.9" fill="none"/></svg> info@pfotenhaus-demo.at
      <svg viewBox="0 0 10 10" aria-hidden="true"><circle cx="5" cy="5" r="4.5"/><path d="M0.5 5 H9.5 M5 0.5 Q2.5 5 5 9.5 M5 0.5 Q7.5 5 5 9.5" stroke="#f0f0f0" stroke-width="0.7" fill="none"/></svg> www. pfotenhaus-demo.at
    </div>
    <div>Sparkasse Hollental Nord,&nbsp; | IBAN: AT 58 1111 2222 3333 4444, | BIC: HLNTAT2H517</div>
  </footer>
</body>
</html>
```